Company service wheel graphic

A graphic demonstrating all the services the company offers.
I have hand drawn and written up on the attached the content that is required. Also attached is our company logo so you have a sense of the colour scheme of the logo.
This will eventually go into a company brochure, be used on our website etc.

Target Market(s)

Local GOvernment and other professionals who work in the sport, recreation and leisure industries

Industry/Entity Type

Sports, recreation, leisure, aquatics

Font styles to use
Other font styles liked:
• Calibri

Colors
0054AA
0677BA
7BADD7
CADEEF
E8F1F8

Requirements
Must have
• An eye catching graphic that captures all the information in the hand drawn atachement.
Nice to have
• Each quadrant in the circle to have its own colour, that links to the company logo

```html
<!DOCTYPE html>
<html lang="en">
<head>
<meta charset="utf-8">
<title>Service Wheel</title>
<link href="https://fonts.googleapis.com/css2?family=Carlito:wght@400;700&display=swap" rel="stylesheet">
<style>
  :root {
    --navy: #0054AA;
    --mid-blue: #0677BA;
    --sky: #7BADD7;
    --sector-strong: #A9C9E7;
    --ring: #CADEEF;
    --pale: #E8F1F8;
    --sector-soft: #DAE8F5;
    --white: #FFFFFF;
  }
  * { box-sizing: border-box; margin: 0; padding: 0; }
  html, body {
    width: 1200px; height: 1195px; overflow: hidden;
    background: var(--white);
    font-family: "Carlito", "Calibri", sans-serif;
  }
  .wheel { position: relative; width: 1200px; height: 1195px; }
  .wheel-shapes { position: absolute; inset: 0; }
  .audience-label {
    font-family: "Carlito", sans-serif;
    font-weight: 700; font-size: 33px; fill: var(--navy);
    letter-spacing: 4px;
  }
  .audience-label.tight { letter-spacing: 0.5px; }
  .service-list { position: absolute; inset: 0; list-style: none; color: var(--navy); font-weight: 700; font-size: 16.5px; line-height: 20px; }
  .service-list li { position: absolute; white-space: nowrap; }
  .service-list .align-end { text-align: right; }
  .bullet { display: inline-block; margin: 0 6px; }
  .spacer { visibility: hidden; }
  .indent { display: inline-block; padding-left: 66px; }
  .category-bar {
    position: absolute; left: 330px; width: 542px; height: 34px;
    background: var(--navy); color: var(--white);
    font-weight: 700; font-size: 19px;
    display: flex; align-items: center; justify-content: center;
  }
  .bar-facilities { top: 377px; }
  .bar-activation { top: 763px; }
  .phase-label { position: absolute; color: var(--navy); font-weight: 700; font-size: 17px; line-height: 20px; text-align: center; }
  .hub {
    position: absolute; left: 497px; top: 492px; width: 206px; height: 206px;
    border-radius: 50%; background: var(--navy); color: var(--white);
    display: flex; align-items: center; justify-content: center; text-align: center;
    font-weight: 700; font-size: 27px; line-height: 31px;
  }
</style>
</head>
<body>
<main class="wheel">
  <svg class="wheel-shapes" width="1200" height="1195" viewBox="0 0 1200 1195">
    <defs>
      <path id="audience-track" d="M 45,597 A 555 555 0 1 1 1155,597 A 555 555 0 1 1 45,597 A 555 555 0 1 1 1155,597"/>
    </defs>
    <circle cx="600" cy="597" r="596" fill="var(--ring)"/>
    <path d="M600,597 L600,1 A596 596 0 0 1 1196,597 Z" fill="var(--sector-strong)"/>
    <path d="M600,597 L600,92 A505 505 0 0 0 95,597 Z" fill="var(--pale)"/>
    <path d="M600,597 L95,597 A505 505 0 0 0 600,1102 Z" fill="var(--sector-soft)"/>
    <path d="M600,597 L600,1102 A505 505 0 0 0 1105,597 Z" fill="var(--pale)"/>
    <line x1="600" y1="1" x2="600" y2="1193" stroke="var(--white)" stroke-width="3"/>
    <line x1="4" y1="597" x2="1196" y2="597" stroke="var(--white)" stroke-width="3"/>
    <rect x="435" y="428" width="330" height="338" fill="var(--sector-soft)"/>
    <rect x="435" y="428" width="163" height="167" fill="var(--pale)"/>
    <rect x="602" y="428" width="163" height="167" fill="var(--sector-strong)"/>
    <rect x="435" y="599" width="163" height="167" fill="var(--pale)"/>
    <rect x="602" y="599" width="163" height="167" fill="var(--sector-soft)"/>
    <text class="audience-label"><textPath href="#audience-track" startOffset="285">LOCAL + STATE GOVERNMENT</textPath></text>
    <text class="audience-label"><textPath href="#audience-track" startOffset="819">SPORT + LEISURE FACILITY MANAGERS</textPath></text>
    <text class="audience-label tight"><textPath href="#audience-track" startOffset="1750">INVESTORS, DEVELOPERS, ARCHITECTS + DESIGNERS</textPath></text>
    <text class="audience-label"><textPath href="#audience-track" startOffset="2663">SPORT + RECREATION + COMMUNITY PROVIDER</textPath></text>
  </svg>

  <ul class="service-list list-planning">
    <li style="left:388px;top:103px"><span class="bullet">•</span>Feasibility Studies</li>
    <li style="left:320px;top:148px"><span class="bullet">•</span>Community + Stakeholder<br><span class="bullet spacer">•</span>research</li>
    <li style="left:252px;top:208px"><span class="bullet">•</span>Sport + recreation strategies</li>
    <li style="left:218px;top:252px"><span class="bullet">•</span>Design strategies</li>
    <li style="left:180px;top:302px"><span class="bullet">•</span>Indoor + outdoor spaces</li>
  </ul>

  <ul class="service-list list-management">
    <li style="left:688px;top:92px">Activating<span class="bullet">•</span><br>underutilised assets</li>
    <li style="left:717px;top:142px">Income + revenue<span class="bullet">•</span><br>generation strategies</li>
    <li style="left:737px;top:192px">Mystery shopper + business<span class="bullet">•</span><br><span class="indent">health check</span></li>
    <li style="left:752px;top:240px">Financial + funding strategies<span class="bullet">•</span></li>
    <li style="left:810px;top:270px">Management support<span class="bullet">•</span></li>
    <li style="left:835px;top:298px">Business planning<span class="bullet">•</span></li>
  </ul>

  <ul class="service-list list-participation">
    <li style="left:90px;top:640px"><span class="bullet">•</span>Trends + insights</li>
    <li style="left:90px;top:688px"><span class="bullet">•</span>Health profiling</li>
    <li style="left:109px;top:738px"><span class="bullet">•</span>Active recreation<br><span class="bullet spacer">•</span>strategies</li>
    <li style="left:128px;top:806px"><span class="bullet">•</span>Community<br><span class="bullet spacer">•</span>program<br><span class="bullet spacer">•</span>development</li>
    <li style="left:217px;top:928px"><span class="bullet">•</span>Physical activity strategies</li>
    <li style="left:245px;top:970px"><span class="bullet">•</span>Specific cohort strategies</li>
    <li style="left:284px;top:1010px"><span class="bullet">•</span>Sports + program<br><span class="bullet spacer">•</span>Specific strategies</li>
  </ul>

  <ul class="service-list list-outcomes">
    <li class="align-end" style="right:70px;top:636px">Community impact<span class="bullet">•</span><br>monitoring<span class="bullet spacer">•</span></li>
    <li class="align-end" style="right:78px;top:700px">Social Value<span class="bullet">•</span></li>
    <li class="align-end" style="right:95px;top:746px">Community<span class="bullet">•</span><br>outcomes + KPIs<span class="bullet spacer">•</span></li>
    <li class="align-end" style="right:110px;top:818px">Contract monitoring<span class="bullet">•</span></li>
  </ul>

  <div class="category-bar bar-facilities">Community, Aquatic + Recreation Facilities</div>
  <div class="category-bar bar-activation">Community Activation</div>

  <div class="phase-label" style="left:450px;top:438px;width:90px">Planning</div>
  <div class="phase-label" style="left:638px;top:438px;width:110px">Management</div>
  <div class="phase-label" style="left:505px;top:713px;width:100px">Growing<br>Participation</div>
  <div class="phase-label" style="left:634px;top:700px;width:130px">Community<br>Impact +<br>Outcomes</div>

  <div class="hub">Community<br>+<br>Stakeholder<br>Engagement</div>
</main>
</body>
</html>
```